Harbor Crest Home Surveys Brochure Design

Upscale Modern Clean Brochure. Our current brochure is about 11 inches high. I will be attaching the source files for our current design HarborSurveyBrochureV8HighRes (all of the information in this design will need to be in final product) . Its a booklet brochure and you can see the style and color or our branding ( For further branding or images please see harborcrestsurveys.com). We are interested in seeing variations of this layout as well as the same information in a bifold design like this example CommercialBrochureCover.png. Bifold design would be 4 total pages. Brochure design would be around 8 pages. Ive also included an older version of our brochure HC_TriFold_2020 (1)-edit (1). We are interested in seeing other front photos that would position us as an authority leader in the home inspection space.

Target Market(s)

Real Estate Agents

Industry/Entity Type

Home Inspections

Other font styles liked:
• https://filedropzy.com/downloads/a417e2b9c03d58f61a2e7b94c0d53f1720221012222612/7bc9034e1d62a58f0c4e31b7a9f2d06520221012222646/kq74mp

Requirements
Must have
• Branded colors of blue that is in our Logo- All of the information that is in the HarborSurveyBrochureV8LowRes- There is also a filedropzy link under the font section that can download source files for this brochure

```html
<!DOCTYPE html>
<html lang="en">
<head>
<meta charset="utf-8">
<title>Harbor Crest Home Surveys – Inspection Brochure Spread</title>
<link href="https://fonts.googleapis.com/css2?family=Archivo:wght@700;800&family=Open+Sans:wght@300;400;600;700&display=swap" rel="stylesheet">
<style>
  :root{
    --brand-blue:#1a6db5;
    --ribbon-blue:#1669b8;
    --paper:#ffffff;
    --grass-light:#6fa63a;
    --grass:#3f8a22;
    --grass-deep:#2e6e17;
    --stage:#f3f3f3;
    --ink-white:#ffffff;
  }
  *{box-sizing:border-box;margin:0;padding:0}
  html,body{width:1200px;height:880px;overflow:hidden;background:var(--stage)}
  body{font-family:"Open Sans",sans-serif;position:relative}

  .spread{position:absolute;left:10px;top:247px;width:1180px;height:386px;display:flex;box-shadow:0 10px 30px rgba(0,0,0,.18)}
  .page{position:relative;width:590px;height:386px;overflow:hidden}

  /* left page */
  .photo-inspector{position:absolute;left:0;top:0;width:290px;height:386px;
    background:linear-gradient(180deg,#b7b0a3 0%,#9a948b 22%,#85827f 45%,#6f6e6e 100%)}
  .brand-mark{position:absolute;left:14px;top:24px;display:flex;align-items:center;gap:6px;
    font-weight:700;font-size:11px;color:var(--ink-white);letter-spacing:.3px}
  .brand-mark .dot{width:16px;height:16px;border-radius:50%;border:1.5px solid var(--ink-white)}
  .standard-panel{position:absolute;left:290px;top:0;width:300px;height:386px;background:var(--brand-blue)}
  .rule{position:absolute;height:1px;background:rgba(255,255,255,.85)}
  .standard-panel .rule{left:16px;right:14px;top:34px}
  .intro{position:absolute;left:18px;top:48px;color:var(--ink-white);line-height:1.15}
  .intro .lead{font-weight:300;font-size:10.5px}
  .intro .name{font-family:"Archivo",sans-serif;font-weight:800;font-size:12px;display:block}
  .feature{position:absolute;left:14px;right:12px}
  .ribbon-white{background:var(--paper);color:var(--ribbon-blue);font-family:"Archivo",sans-serif;font-weight:800;
    font-size:10px;padding:3px 10px;letter-spacing:.2px;text-transform:uppercase}
  .feature p{color:var(--ink-white);font-size:7.3px;line-height:1.35;margin-top:4px;padding-left:10px}
  .with-thumb{display:flex;gap:9px;margin-top:6px}
  .with-thumb p{margin-top:2px;padding-left:0;flex:1}
  .thumb{flex:none;width:92px;height:58px}
  .thumb-tablet{background:linear-gradient(135deg,#4b4f55,#9fa6ad 60%,#d9dde1)}
  .thumb-camera{background:linear-gradient(135deg,#b9bcbf,#8e9296 60%,#3a3d40)}

  /* right page */
  .photo-lawn{position:absolute;inset:0;
    background:radial-gradient(ellipse at 45% 18%,#cfe1c2 0%,rgba(160,200,130,.6) 18%,transparent 45%),
               linear-gradient(180deg,var(--grass-light) 0%,var(--grass) 45%,var(--grass-deep) 100%)}
  .illustration-house{position:absolute;left:330px;top:14px;width:240px;height:150px;
    background:linear-gradient(160deg,#e9e4dc,#c9b9a2 55%,#8c8f94);clip-path:polygon(30% 0,78% 4%,100% 40%,96% 92%,55% 100%,4% 80%,0 38%)}
  .plus-panel .rule{left:26px;right:20px;top:30px}
  .plus-intro{position:absolute;left:24px;top:100px;color:var(--ink-white)}
  .plus-intro .lead{font-weight:300;font-size:10px}
  .plus-intro .name{font-family:"Archivo",sans-serif;font-weight:800;font-size:11px}
  .plus-intro .sub{font-weight:700;font-size:6.3px;margin-top:3px;width:280px;line-height:1.3}
  .ribbon-blue{background:var(--ribbon-blue);color:var(--ink-white);font-family:"Archivo",sans-serif;font-weight:800;
    font-size:10px;padding:3px 12px;text-transform:uppercase;letter-spacing:.2px}
  .plus-item{position:absolute}
  .plus-item p{color:var(--ink-white);font-size:7.2px;line-height:1.35;margin-top:4px;padding-left:12px}
  .col-a{left:22px;width:292px}
  .col-b{left:330px;width:240px}
</style>
</head>
<body>
<main class="spread">

  <section class="page page-standard">
    <div class="photo-inspector" role="img" aria-label="Inspector in company cap and jacket crouching on a suburban street, flying an inspection drone"></div>
    <div class="brand-mark"><span class="dot"></span>Harbor Crest Home Surveys</div>

    <div class="standard-panel">
      <div class="rule"></div>
      <div class="intro">
        <span class="lead">Here’s what’s included in our</span>
        <span class="name">Harbor Standard Home Inspection</span>
      </div>

      <div class="feature" style="top:82px">
        <div class="ribbon-white">Certified Inspectors</div>
        <p>All inspections are performed by inspectors who are certified by the industry’s leading trade organization.</p>
      </div>

      <div class="feature" style="top:130px">
        <div class="ribbon-white">In-Depth Inspection</div>
        <p>Over 1,800 items in the house are checked during a Harbor inspection, including the plumbing, heating, air conditioning, and electrical systems, the foundation, structure, roof, and property grounds.</p>
      </div>

      <div class="feature" style="top:190px">
        <div class="ribbon-white">Comprehensive Inspection Report</div>
        <div class="with-thumb">
          <div class="thumb thumb-tablet" role="img" aria-label="Hands holding a tablet showing a digital inspection report with photos"></div>
          <p>A professional, digital-format inspection report, complete with detailed photos and a summary page – all delivered within 24 hours of the inspection.</p>
        </div>
      </div>

      <div class="feature" style="top:282px">
        <div class="ribbon-white">Whole-House Infrared Scans</div>
        <div class="with-thumb">
          <div class="thumb thumb-camera" role="img" aria-label="Hand holding a thermal imaging camera"></div>
          <p>Extensive infrared scans help us detect air duct leakage, electrical hotspots, and hidden moisture – all problems that are not apparent to the naked eye.</p>
        </div>
      </div>
    </div>
  </section>

  <section class="page page-plus plus-panel">
    <div class="photo-lawn" role="img" aria-label="Lawn sprinkler head spraying water over green grass"></div>
    <div class="illustration-house" role="img" aria-label="Cutaway illustration of a two-storey house showing rooms and garage"></div>
    <div class="rule"></div>

    <div class="plus-intro">
      <div><span class="lead">Here’s what’s included in our </span><span class="name">Harbor PLUS Home Inspection</span></div>
      <div class="sub">Our Harbor PLUS Home Inspection includes everything in the Standard Inspection, plus these additional services:</div>
    </div>

    <div class="plus-item col-a" style="top:140px">
      <div class="ribbon-blue">Multiple Guarantees</div>
      <p>Harbor provides a unique set of 100-day limited guarantees covering the structural &amp; mechanical inspection, the roof condition &amp; no-leak inspection, the mold inspection, and the underground sewer/water line inspection.</p>
    </div>

    <div class="plus-item col-a" style="top:200px">
      <div class="ribbon-blue">Home Maintenance Book</div>
      <p>Inspection clients receive a free copy of the book, “Living Well in Your New Home,” which offers home maintenance tips for keeping your home safe and in top condition.</p>
    </div>

    <div class="plus-item col-a" style="top:258px">
      <div class="ribbon-blue">FixQuote</div>
      <p>Your Harbor inspection report will detail the deficiencies in the home, but that leaves most homebuyers wondering how much it would cost to remedy all of those deficiencies. A FixQuote report provides that information quickly and easily.</p>
    </div>

    <div class="plus-item col-a" style="top:322px">
      <div class="ribbon-blue">Sprinkler &amp; Irrigation Inspection</div>
      <p>This is a valuable add-on inspection that examines the home’s landscape irrigation system, including one control box and all visible sprinkler heads.</p>
    </div>

    <div class="plus-item col-b" style="top:176px">
      <div class="ribbon-blue">$50 Off Ancillary Inspections</div>
      <p>With a Harbor PLUS inspection, you get $50 OFF a sewer camera inspection, roof certification, or an indoor air quality inspection.</p>
    </div>

    <div class="plus-item col-b" style="top:240px">
      <div class="ribbon-blue">50% Off Maintenance Inspection</div>
      <p>As a Harbor PLUS customer, you’re entitled to 50% OFF your first year Annual Maintenance Inspection!</p>
    </div>

    <div class="plus-item col-b" style="top:322px">
      <div class="ribbon-blue">Home Safety Manual</div>
      <p>Each Harbor PLUS inspection package comes with a free copy of “The Secure Household,” an informative 225-page home safety manual (pdf version).</p>
    </div>
  </section>

</main>
</body>
</html>
```